Commercial Piping Company Needs A Modern Business Card

We need a clean business card for our commercial pipe lining company. We would like to see a mock up in two color schemes: Black, Grey and Blue and Black, Grey and Orange. We are in the piping industry, but want a professional, clean and modern look to the card.

Industry/Entity Type

Plumbing

Contact Information for Business Card

Name: Mark Telford
Title: Managing Partner
Phone: 608.352.9174
Email: Mark@VeltaSpan.Net

Requirements
Must have
• Back Side Should Have a White Back Ground with Full Logo. Front I would like to see a couple lay outs for contact info. Also the final card will have rounded edges, so please take that into account for printing.
Nice to have
• Two Color Palette Examples
Should not have
• No need for an address line

```html
<!DOCTYPE html>
<html lang="en">
<head>
<meta charset="utf-8">
<title>VeltaSpan Business Card</title>
<link href="https://fonts.googleapis.com/css2?family=Questrial&display=swap" rel="stylesheet">
<style>
  :root {
    --backdrop: #ece7e1;
    --card: #f7f7f5;
    --ink: #111111;
    --muted: #9a9a9a;
    --shadow: rgba(60, 45, 30, 0.22);
  }
  * { margin: 0; padding: 0; box-sizing: border-box; }
  html, body {
    width: 1200px;
    height: 974px;
    overflow: hidden;
    background: var(--backdrop);
    font-family: "Questrial", "Century Gothic", sans-serif;
    color: var(--ink);
  }
  .stage {
    position: relative;
    width: 1200px;
    height: 974px;
  }
  .card {
    position: absolute;
    top: 150px;
    width: 380px;
    height: 665px;
    background: var(--card);
    border-radius: 14px;
    box-shadow: 0 10px 28px var(--shadow);
    overflow: hidden;
  }
  .card--front { left: 170px; }
  .card--back { left: 650px; }

  .hero-art {
    position: absolute;
    left: 0;
    top: 100px;
    width: 300px;
    height: 250px;
    background: var(--ink);
    border-radius: 0 60% 45% 0 / 0 45% 55% 0;
  }

  .contact {
    position: absolute;
    left: 42px;
    bottom: 62px;
  }
  .contact__name {
    font-size: 21px;
    letter-spacing: 0.5px;
    text-transform: uppercase;
    line-height: 1.1;
  }
  .contact__title {
    font-size: 15px;
    color: var(--muted);
    margin-bottom: 16px;
  }
  .contact__line {
    font-size: 15px;
    line-height: 1.45;
  }

  .brand-lockup {
    position: absolute;
    left: 50%;
    top: 50%;
    transform: translate(-50%, -50%);
    display: flex;
    flex-direction: column;
    align-items: flex-end;
  }
  .brand-lockup__mark {
    width: 58px;
    height: 58px;
    border-radius: 50%;
    background: var(--ink);
    margin-bottom: 8px;
    margin-right: -8px;
  }
  .brand-lockup__text {
    writing-mode: vertical-rl;
    display: flex;
    flex-direction: column;
    text-transform: uppercase;
  }
  .brand-lockup__name {
    font-size: 46px;
    line-height: 1;
    letter-spacing: 1px;
  }
  .brand-lockup__tagline {
    font-size: 19px;
    line-height: 1.1;
    letter-spacing: 0.3px;
  }
</style>
</head>
<body>
<main class="stage">
  <section class="card card--front">
    <div class="hero-art" role="img" aria-label="Black silhouette illustration of an animal head"></div>
    <div class="contact">
      <p class="contact__name">Mark Telford</p>
      <p class="contact__title">Managing Partner</p>
      <p class="contact__line">P. 608.352.9174</p>
      <p class="contact__line">Mark@VeltaSpan.Net</p>
      <p class="contact__line">www.VeltaSpan.Net</p>
    </div>
  </section>

  <section class="card card--back">
    <div class="brand-lockup">
      <div class="brand-lockup__mark"></div>
      <div class="brand-lockup__text">
        <span class="brand-lockup__name">VeltaSpan</span>
        <span class="brand-lockup__tagline">Commercial Pipe Lining Group</span>
        <span class="brand-lockup__tagline">Inspect • Renew • Protect</span>
      </div>
    </div>
  </section>
</main>
</body>
</html>
```